Letterhead for financial advisor-insurance agent firm

Our company, Marlowe Thistle Insurance & Investments, is an insurance (health, life, home, auto, etc) and investment brokerage offering a suite of options to meet client needs. We need letterhead that is professional and embodies strength, security and sophistication.

Industry/Entity Type

Investment

```html
<!DOCTYPE html>
<html lang="en">
<head>
<meta charset="utf-8">
<title>Marlowe Thistle Insurance &amp; Investments — Letterhead</title>
<link rel="stylesheet" href="https://fonts.googleapis.com/css2?family=Cinzel:wght@600&family=Questrial&display=swap">
<style>
  :root {
    --ink-navy: #2b2a48;
    --icon-grey: #5b5d66;
    --paper: #ffffff;
    --backdrop: #ffffff;
  }
  * { box-sizing: border-box; margin: 0; padding: 0; }
  html, body {
    width: 900px;
    height: 1200px;
    overflow: hidden;
    background: var(--backdrop);
  }
  .letterhead {
    position: relative;
    width: 900px;
    height: 1200px;
    background: var(--paper);
  }
  .brand {
    position: absolute;
    left: 22px;
    top: 26px;
    width: 352px;
    text-align: center;
    color: var(--ink-navy);
    font-family: "Cinzel", "Times New Roman", serif;
    font-weight: 600;
  }
  .brand-square {
    display: block;
    width: 98px;
    height: 98px;
    margin: 0 auto 16px;
    border: 3px solid var(--ink-navy);
  }
  .brand-name {
    font-size: 31px;
    line-height: 1;
    letter-spacing: 0.5px;
    white-space: nowrap;
  }
  .brand-tagline {
    margin-top: 5px;
    font-size: 14px;
    line-height: 1;
    letter-spacing: 1px;
  }
  .contact-list {
    position: absolute;
    left: 531px;
    top: 51px;
    list-style: none;
    font-family: "Questrial", "Century Gothic", sans-serif;
    font-size: 23px;
    color: var(--ink-navy);
  }
  .contact-item {
    display: flex;
    align-items: center;
    height: 29.5px;
    white-space: nowrap;
  }
  .contact-icon {
    width: 30px;
    height: 26px;
    margin-right: 4px;
    fill: var(--icon-grey);
    stroke: var(--icon-grey);
  }
  .header-rule {
    position: absolute;
    left: 0;
    top: 209px;
    width: 900px;
    height: 13px;
    background: var(--ink-navy);
  }
</style>
</head>
<body>
<main class="letterhead">
  <header>
    <div class="brand">
      <span class="brand-square" aria-hidden="true"></span>
      <div class="brand-name">Marlowe Thistle</div>
      <div class="brand-tagline">Insurance &amp; Investments</div>
    </div>

    <ul class="contact-list">
      <li class="contact-item">
        <svg class="contact-icon" viewBox="0 0 30 26" aria-hidden="true">
          <path stroke="none" d="M6 3c1.5-1 3-1 3.8.4l2.2 3.6c.6 1 .3 2-.6 2.6l-1.6 1c1 2.6 3.2 5 5.8 6.2l1.1-1.5c.7-.9 1.8-1 2.7-.4l3.5 2.4c1.1.8 1.2 2.2.2 3.4-1.5 1.8-3.5 2.4-5.8 1.5C10 19.8 5.5 14.5 4 9c-.6-2.4.2-4.6 2-6z"/>
        </svg>
        1742 318 604
      </li>
      <li class="contact-item">
        <svg class="contact-icon" viewBox="0 0 30 26" aria-hidden="true">
          <rect x="3" y="6" width="24" height="16" rx="1.5" fill="none" stroke-width="2.2"/>
          <path d="M3.5 7l11.5 8.5L26.5 7" fill="none" stroke-width="2.2"/>
        </svg>
        info@marlowethistle.com
      </li>
      <li class="contact-item">
        <svg class="contact-icon" viewBox="0 0 30 26" aria-hidden="true">
          <g fill="none" stroke-width="1.8">
            <circle cx="15" cy="13" r="10"/>
            <ellipse cx="15" cy="13" rx="4.5" ry="10"/>
            <path d="M5 13h20M6.5 8h17M6.5 18h17"/>
          </g>
        </svg>
        www.marlowethistle.com
      </li>
      <li class="contact-item">
        <svg class="contact-icon" viewBox="0 0 30 26" aria-hidden="true">
          <path stroke="none" d="M15 2L2 13.5h3.5V24h7.5v-7h4v7h7.5V13.5H28z"/>
        </svg>
        P.O. Box 48207, elm street, NY
      </li>
    </ul>
  </header>
  <div class="header-rule" aria-hidden="true"></div>
</main>
</body>
</html>
```